BKT Consulting

Government/Entitlement Consulting Services- I assist developers obtain entitlements from local, state and federal government agencies so that they can build their projects. Often these projects are very complicated and political and may face community opposition.

Target Market(s)

Real Estate Developers

Industry/Entity Type

Business Consultant

Contact Information for Business Card

Dana Velmonte
Principal

Font styles to use
Serif
Sans Serif

Requirements
Must have
• Classy and professional appeal.
Nice to have
• I like a combination of a mat and glossy finish. I've seen that done with black and then a bold color for a pop, but am not 100% committed to that.

```html
<!DOCTYPE html>
<html lang="en">
<head>
<meta charset="utf-8">
<title>BKT Consulting – Business Cards</title>
<link rel="stylesheet" href="https://fonts.googleapis.com/css2?family=Noto+Serif:wght@400;700&family=Roboto:wght@400;500&display=swap">
<style>
  :root {
    --bg: #3b332e;
    --card-dark: #0c0c0d;
    --card-dark-edge: #1c1c1e;
    --card-light: #ffffff;
    --accent: #1b8fd2;
    --ink: #111111;
  }
  * { box-sizing: border-box; margin: 0; padding: 0; }
  html, body {
    width: 1200px;
    height: 716px;
    overflow: hidden;
    background: var(--bg);
  }
  .canvas {
    position: relative;
    width: 1200px;
    height: 716px;
    display: flex;
    align-items: center;
    justify-content: center;
    gap: 48px;
  }
  .card {
    width: 520px;
    height: 297px;
    border-radius: 10px;
    position: relative;
    box-shadow: 0 10px 28px rgba(0,0,0,0.45);
  }
  .card--front {
    background: radial-gradient(ellipse at 45% 40%, var(--card-dark-edge), var(--card-dark) 70%);
    display: flex;
    align-items: center;
    justify-content: center;
  }
  .card--back {
    background: var(--card-light);
  }
  .wordmark {
    font-family: "Noto Serif", serif;
    font-weight: 700;
    color: var(--accent);
    letter-spacing: 1px;
    white-space: nowrap;
  }
  .card--front .wordmark { font-size: 40px; }
  .card--back .wordmark {
    position: absolute;
    left: 38px;
    top: 78px;
    font-size: 30px;
  }
  .contact {
    position: absolute;
    left: 300px;
    top: 150px;
  }
  .contact__name {
    font-family: "Noto Serif", serif;
    font-size: 21px;
    color: var(--ink);
    line-height: 1.1;
  }
  .contact__title {
    font-family: "Roboto", sans-serif;
    font-size: 14px;
    color: var(--accent);
    margin-bottom: 10px;
  }
  .contact__row {
    display: flex;
    align-items: flex-start;
    gap: 7px;
    font-family: "Roboto", sans-serif;
    font-size: 13px;
    color: var(--ink);
    line-height: 1.3;
    margin-bottom: 3px;
  }
  .contact__icon {
    width: 11px;
    height: 11px;
    margin-top: 3px;
    flex: none;
    fill: var(--accent);
  }
</style>
</head>
<body>
  <main class="canvas">
    <section class="card card--front" aria-label="Business card front">
      <span class="wordmark">BKT Consulting</span>
    </section>

    <section class="card card--back" aria-label="Business card back">
      <span class="wordmark">BKT Consulting</span>
      <div class="contact">
        <p class="contact__name">Dana Velmonte</p>
        <p class="contact__title">Job Title</p>
        <div class="contact__row">
          <svg class="contact__icon" viewBox="0 0 12 12" aria-hidden="true">
            <path d="M6 0a4 4 0 0 0-4 4c0 3 4 8 4 8s4-5 4-8a4 4 0 0 0-4-4zm0 5.6A1.6 1.6 0 1 1 6 2.4a1.6 1.6 0 0 1 0 3.2z"/>
          </svg>
          <span>00, Steet name<br>City, St. 00000</span>
        </div>
        <div class="contact__row">
          <svg class="contact__icon" viewBox="0 0 12 12" aria-hidden="true">
            <path d="M1 3.5C1 2.5 3 1.5 6 1.5s5 1 5 2v1H8.5V3.6h-5v.9H1z"/>
            <path d="M2.5 5.5h7l1 4.5h-9z"/>
          </svg>
          <span>000 000 0000</span>
        </div>
        <div class="contact__row">
          <svg class="contact__icon" viewBox="0 0 12 12" aria-hidden="true">
            <path d="M0.5 2.5h11v7h-11z M1 3l5 3.6L11 3" />
          </svg>
          <span>youremail@xyz.com</span>
        </div>
      </div>
    </section>
  </main>
</body>
</html>
```